Popup Nightclub Grand Opening Flyer

We need to design a flyer for the grand opening of an upscale, exclusive nightclub called "Lanternfall". The design needs to be chic and exclusive. The background should be black and the text should primarily be white. We like minimalist designs.

Here is the text for the flyer
-
Velvetrope Atlanta Presents

Lanternfall (LOGO)

A Popup Nightclub Experience
For one night Only

Friday, October 18, 2013
Party begins at 9PM

INVITE ONLY

See invitation for location details
(Velvetrope Atlanta logo)

-
Examples we like

http://cdn2-b.brivelpost.com/sites/default/files/styles/image_content_width/hash/3d/fa/1472093815_4471_flyer.jpg?itok=R8kqWm2z

http://api.plovra.com/files/7Kqq-Tr82XXB3pQzJvmtR5HL2W719E4nbRtC6KLd4HsfM8Y2qTDK-VmjwDoNqLX4QBzTHD9nakRbVx3m-Pfq8htc3MDTWr5p4/2zelSaturdays.jpg

http://quenmar.com/wp-content/uploads/yootheme/widgetkit/gallery/2zel/2zel-gen_vroom4-01.jpg

Hi All, one thing that we are seeing that we don't like is on over emphasis on the phrase "a popup nightclub experience" please don't make this the largest thing on the flyer

Target Market(s)

Target market is 25-35 year olds who are affluent (rich) and like luxury brands

Requirements
Must have
• Dark Background
Nice to have
• Velvetrope Logo on the bottom
Modern text that isn't curvy
Should not have
• Curved text

```html
<!DOCTYPE html>
<html lang="en">
<head>
<meta charset="utf-8">
<title>Velvetrope Atlanta presents Lanternfall Nightclub</title>
<link rel="stylesheet" href="https://fonts.googleapis.com/css2?family=Syncopate:wght@400;700&family=Josefin+Sans:wght@300;400&display=swap">
<style>
  :root {
    --paper: #ffffff;
    --ink-black: #050505;
    --glow: #3b3d40;
    --white: #f4f4f4;
    --steel: #9aa3ad;
    --steel-light: #c9ced4;
    --rule: #8c8f93;
    --edge: #5b4d8c;
    --band-light: #e2e4e6;
    --band-dark: #8f9397;
    --band-text: #1a1a1a;
  }
  * { margin: 0; padding: 0; box-sizing: border-box; }
  html, body {
    width: 956px;
    height: 1200px;
    overflow: hidden;
    background: var(--paper);
  }
  .flyer {
    position: absolute;
    left: 36px;
    top: 28px;
    width: 880px;
    height: 1142px;
    background: radial-gradient(ellipse 60% 50% at 50% 36%, var(--glow) 0%, #1c1d1f 55%, var(--ink-black) 100%);
    outline: 2px solid var(--edge);
    color: var(--white);
    text-align: center;
    font-family: "Syncopate", sans-serif;
  }
  .presenter {
    position: absolute;
    top: 112px;
    width: 100%;
    font-size: 34px;
    line-height: 38px;
    letter-spacing: 1px;
  }
  .presenter .city { color: var(--steel); }
  .venue-mark {
    position: absolute;
    top: 262px;
    width: 100%;
  }
  .venue-mark .dot {
    display: block;
    margin: 0 auto;
    width: 110px;
    height: 110px;
    border-radius: 50%;
    background: radial-gradient(circle at 40% 35%, var(--steel-light), #7d848b);
  }
  .venue-name {
    margin-top: 46px;
    font-family: "Josefin Sans", sans-serif;
    font-weight: 300;
    color: var(--white);
    font-size: 58px;
    letter-spacing: 10px;
    line-height: 60px;
    padding-left: 10px;
  }
  .venue-kind {
    margin-top: 10px;
    font-family: "Josefin Sans", sans-serif;
    font-weight: 300;
    color: var(--white);
    font-size: 30px;
    letter-spacing: 5px;
    padding-left: 5px;
  }
  .headline {
    position: absolute;
    top: 596px;
    width: 100%;
    font-size: 42px;
    line-height: 40px;
  }
  .headline strong {
    font-weight: 700;
    color: var(--steel-light);
  }
  .rule {
    position: absolute;
    left: 200px;
    width: 474px;
    height: 12px;
  }
  .rule-top { top: 838px; }
  .rule-bottom { top: 952px; }
  .details {
    position: absolute;
    top: 862px;
    width: 100%;
    font-size: 19px;
    line-height: 24px;
    font-family: "Syncopate", sans-serif;
  }
  .access {
    position: absolute;
    top: 912px;
    width: 100%;
    font-family: "Josefin Sans", sans-serif;
    font-weight: 300;
    font-size: 38px;
    letter-spacing: 3px;
  }
  .contact-band {
    position: absolute;
    left: 0;
    top: 1050px;
    width: 100%;
    height: 34px;
    background: linear-gradient(180deg, var(--band-light) 0%, #b9bcc0 50%, var(--band-dark) 100%);
    color: var(--band-text);
    font-size: 14px;
    line-height: 34px;
    font-weight: 700;
    letter-spacing: 0.5px;
  }
</style>
</head>
<body>
  <main class="flyer">
    <header class="presenter">
      <div>VELVETROPE</div>
      <div class="city">ATLANTA</div>
      <div>PRESENTS</div>
    </header>

    <section class="venue-mark">
      <span class="dot"></span>
      <div class="venue-name">LANTERNFALL</div>
      <div class="venue-kind">NIGHTCLUB</div>
    </section>

    <h1 class="headline">
      <div>A POPUP</div>
      <strong>NIGHTCLUB</strong><br>
      <strong>EXPERIENCE</strong>
      <div>FOR ONE</div>
      <div>NIGHT ONLY</div>
    </h1>

    <svg class="rule rule-top" viewBox="0 0 474 12" aria-hidden="true">
      <line x1="0" y1="6" x2="474" y2="6" stroke="var(--rule)" stroke-width="1.5"/>
      <circle cx="237" cy="6" r="4" fill="var(--steel-light)"/>
    </svg>

    <p class="details">
      Friday, October 18, 2013<br>
      Party begins at 9PM
    </p>

    <p class="access">INVITE ONLY</p>

    <svg class="rule rule-bottom" viewBox="0 0 474 12" aria-hidden="true">
      <line x1="0" y1="6" x2="474" y2="6" stroke="var(--rule)" stroke-width="1.5"/>
      <circle cx="237" cy="6" r="4" fill="var(--steel-light)"/>
    </svg>

    <footer class="contact-band">
      address: xxxxxxxxxxxxxxxx xxxxxxxx Ph: 0000 0000 0000 W: dummywebsite.com
    </footer>
  </main>
</body>
</html>
```